Start-up braucht modernes/hochwertiges Getränkeetikett
Zielgruppe
Wir sind ein modernes, nachhaltiges Start-up, welches eine neue Getränkekategorie auf den Markt bringt. Ein sogenanntes Elektrolyt-Getränk mit dem Namen KLORV5. Es ist abgefüllt in eine 500 ml Flasche und enthält Magnesium, Kalzium, Kalium, und Natrium. Diese Stoffe (Elektrolyte) dienen der körperlichen Hydrierung. Zu Dehydrierung kann es durch Hitze, Alkohol, Sport oder Krankheit kommen. Krankheit liegt bei uns allerdings nicht im Fokus. In unserer Zielgruppe befinden sich hauptsächlich Personen im Alter von 18 - 29 Jahren.
Die Geschmacksrichtung ist Zitrone-Limette.
Aufgabenstellung
Das Etikett soll:
- MODERN, SCHLICHT und HOCHWERTIG sein, so dass es im Supermarkt hervorsticht
- erkenntlich machen, dass die Stoffe Magnesium, Natrium, Kalzium und Kalium enthalten sind
- sich farblich deutlich von der Farbe des Inhalts (weiß) abheben. (Vorzugsweise mit einem hellen Blau, türkis)
- für unsere junge Zielgruppe ansprechend sein
- ebenfalls auf die Geschmacksrichtung (Zitrone-Limette) hinweisen, und zwar so, dass wenn man eine weitere Geschmacksrichtung auf den Markt bringen möchte, diese leicht angepasst werden kann.
- nicht nach einem Energydrink oder einem typischen Sportgetränk aussehen
- unter dem Namen den Slogan 'Elektrolyt-Getränk' stehen haben
-Das Etikett ist nicht dursichtig sondern besteht aus Papier
Der Name sowie das Logo können selbstverständlich farblich verändert werden. Bei dem Logo können auch größere Änderungen vollzogen werden.
Bitte beachten Sie die unten zu stehenden Regler um sich einen guten Überblick über unsere Vorstellungen zu verschaffen. Die Platzierung des EAN-Code ist für ihr Design irrelevat .
Bei Unklarheiten gerne nachfragen!

```html
<!DOCTYPE html>
<html lang="de">
<head>
<meta charset="utf-8">
<title>KLORV5 – Elektrolyt-Getränk Etikett</title>
<link href="https://fonts.googleapis.com/css2?family=Roboto+Slab:wght@300;600;700;800&display=swap" rel="stylesheet">
<style>
  :root {
    --ice: #d4ebf1;
    --swirl: #b7dfe8;
    --ink: #1d1d1b;
    --lime: #d2dc5a;
  }
  html, body {
    margin: 0;
    padding: 0;
    overflow: hidden;
  }
  body {
    width: 1200px;
    height: 523px;
    font-family: "Roboto Slab", serif;
    color: var(--ink);
  }
  .label {
    position: relative;
    width: 1200px;
    height: 523px;
    overflow: hidden;
    background: var(--ice);
  }
  .marble-pattern {
    position: absolute;
    inset: 0;
    background:
      radial-gradient(ellipse 260px 120px at 12% 40%, var(--swirl), transparent 70%),
      radial-gradient(ellipse 300px 140px at 88% 30%, var(--swirl), transparent 70%),
      radial-gradient(ellipse 240px 110px at 80% 85%, var(--swirl), transparent 70%),
      radial-gradient(ellipse 220px 100px at 20% 90%, var(--swirl), transparent 70%),
      linear-gradient(135deg, var(--ice), #c9e6ee 50%, var(--ice));
  }
  .brand-mark {
    position: absolute;
    left: 0;
    top: 0;
  }
  .brand-name {
    position: absolute;
    left: 0;
    width: 1282px;
    top: 124px;
    margin: 0;
    text-align: center;
    font-weight: 800;
    font-size: 48px;
    line-height: 56px;
    letter-spacing: 1px;
  }
  .info-table {
    position: absolute;
    left: 0;
    top: 0;
  }
  .tagline {
    position: absolute;
    left: 420px;
    width: 442px;
    top: 226px;
    margin: 0;
    text-align: center;
    font-weight: 700;
    font-size: 30px;
    line-height: 34px;
  }
  .row-label {
    position: absolute;
    left: 465px;
    margin: 0;
    font-weight: 600;
    font-size: 21px;
    line-height: 26px;
  }
  .row-label--flavour { top: 288px; }
  .row-label--ingredients { top: 341px; }
  .flavour-value {
    position: absolute;
    left: 673px;
    top: 287px;
    margin: 0;
    font-weight: 300;
    font-size: 22px;
    line-height: 28px;
  }
  .ingredient-list {
    position: absolute;
    left: 672px;
    top: 342px;
    margin: 0;
    padding: 0;
    list-style: none;
    font-weight: 300;
    font-size: 22px;
    line-height: 25.7px;
  }
</style>
</head>
<body>
  <main class="label">
    <div class="marble-pattern" role="img" aria-label="Marmorierter Hintergrund in hellem Türkis mit fließenden blauen Wirbeln"></div>

    <svg class="brand-mark" width="1200" height="523" aria-hidden="true">
      <circle cx="641" cy="72" r="37" fill="none" stroke="var(--ink)" stroke-width="2"/>
    </svg>

    <h1 class="brand-name">KLORV5</h1>

    <svg class="info-table" width="1200" height="523" aria-hidden="true">
      <polygon points="662,288 837,287 830,315 656,316" fill="var(--lime)"/>
      <g fill="none" stroke="var(--ink)" stroke-width="1.6">
        <rect x="420.5" y="207.5" width="441" height="260"/>
        <line x1="420" y1="278" x2="862" y2="278"/>
        <line x1="420" y1="325.5" x2="862" y2="325.5"/>
        <line x1="640" y1="278" x2="640" y2="467"/>
      </g>
    </svg>

    <p class="tagline">Elektrolyt-Getränk</p>

    <p class="row-label row-label--flavour">Geschmack:</p>
    <p class="flavour-value">Zitrone-Limette</p>

    <p class="row-label row-label--ingredients">Inhaltstoffe<br>die dich fit<br>halten:</p>
    <ul class="ingredient-list">
      <li>+ Magnesium</li>
      <li>+ Natrium</li>
      <li>+ Kalzium</li>
      <li>+ Kalium</li>
    </ul>
  </main>
</body>
</html>
```